Flyer Design Project

Advertising - The header is the most important thing on this flyer, I would like to see an eyes-popping more in dept look of the clouds along with the sport car of the couple on the road. The symbol of the "Lantern of Quiet Orchards" don't want it there. Just replace it with a regular "i".

Industry/Entity Type

Advertising

Requirements
Must have
• head turning... stopping prospects to read the flyer... everything got to be on point from art works to different fonts and style.

```html
<!DOCTYPE html>
<html lang="en">
<head>
<meta charset="UTF-8">
<title>Lantern of Quiet Orchards</title>
<link href="https://fonts.googleapis.com/css2?family=Montserrat:ital,wght@1,900&family=Open+Sans:ital,wght@0,300;0,400;0,700;1,300;1,400&family=Source+Sans+3:ital,wght@0,700;1,700&display=swap" rel="stylesheet">
<style>
  :root {
    --sky-top: #8cbde6;
    --sky-mid: #d4e7f6;
    --ink: #1d1d1f;
    --brand-blue: #1a73cf;
    --brand-red: #e11d23;
    --badge-orange: #efb85a;
    --badge-edge: #e2774a;
    --badge-text: #7a3410;
    --column-top: #58a6ef;
    --column-bottom: #3f78b4;
    --footer-navy: #1b2552;
    --white: #ffffff;
  }
  * { margin: 0; padding: 0; box-sizing: border-box; }
  html, body { width: 960px; height: 1200px; overflow: hidden; }
  body {
    position: relative;
    font-family: "Open Sans", sans-serif;
    color: var(--ink);
    background: var(--white);
  }
  .sky {
    position: absolute; inset: 0 0 110px 0;
    background:
      radial-gradient(ellipse 300px 120px at 120px 60px, rgba(255,255,255,.9), transparent 70%),
      radial-gradient(ellipse 360px 140px at 700px 40px, rgba(255,255,255,.85), transparent 70%),
      radial-gradient(ellipse 420px 200px at 300px 420px, rgba(255,255,255,.9), transparent 70%),
      radial-gradient(ellipse 400px 260px at 250px 800px, rgba(255,255,255,.95), transparent 70%),
      linear-gradient(180deg, var(--sky-top) 0%, var(--sky-mid) 30%, #eef5fb 60%, var(--white) 100%);
  }
  .road-scene {
    position: absolute; left: 630px; top: 120px; width: 330px; height: 290px;
    background: radial-gradient(ellipse at 55% 50%, #c98a78 0%, #b6c3d0 40%, rgba(220,232,243,.6) 65%, transparent 80%);
  }
  .headline {
    position: absolute; left: 0; top: 0; width: 960px;
    font-family: "Montserrat", sans-serif; font-style: italic; font-weight: 900;
    text-transform: uppercase; line-height: 1;
  }
  .headline span { position: absolute; white-space: nowrap; }
  .headline .line-small { left: 140px; top: 52px; font-size: 54px; color: var(--ink); letter-spacing: -1px; }
  .headline .line-big { left: 66px; top: 94px; font-size: 112px; color: var(--brand-blue); letter-spacing: -2px; }
  .headline .line-red { left: 312px; top: 182px; font-size: 64px; color: var(--brand-red); letter-spacing: -1px; }
  .tagline { position: absolute; left: 112px; top: 244px; font-size: 23px; font-style: italic; font-weight: 300; white-space: nowrap; }

  .heading { position: absolute; left: 64px; font-family: "Source Sans 3", sans-serif; font-weight: 700; white-space: nowrap; }
  .intro-title { top: 306px; font-size: 30px; line-height: 27px; }
  .how-title { top: 522px; font-size: 30px; text-transform: uppercase; }
  .never-title { top: 728px; font-size: 33px; text-transform: uppercase; }

  .copy { position: absolute; left: 64px; font-size: 16px; font-weight: 300; line-height: 21.6px; white-space: nowrap; }
  .copy strong { font-weight: 700; }
  .intro-copy { top: 374px; }
  .system-copy { top: 460px; }

  .steps { list-style: none; }
  .steps li { position: absolute; left: 70px; padding-left: 48px; font-size: 16px; font-weight: 300; line-height: 21.6px; white-space: nowrap; }
  .steps li:nth-child(1) { top: 579px; }
  .steps li:nth-child(2) { top: 622px; }
  .steps li:nth-child(3) { top: 665px; }
  .step-num {
    position: absolute; left: 0; top: -7px; width: 36px; height: 36px; border-radius: 50%;
    background: var(--brand-blue); color: var(--white); font-weight: 700; font-size: 19px;
    display: flex; align-items: center; justify-content: center;
  }
  .benefits { position: absolute; left: 70px; top: 776px; list-style: none; }
  .benefits li { position: relative; padding-left: 22px; font-size: 16px; font-weight: 300; line-height: 21.6px; margin-bottom: 8.4px; white-space: nowrap; }
  .benefits li svg { position: absolute; left: 0; top: 1px; }
  .benefits em { font-style: normal; font-weight: 700; color: var(--brand-red); }

  .info-column {
    position: absolute; left: 645px; top: 500px; width: 268px; height: 590px;
    background: linear-gradient(180deg, var(--column-top), var(--column-bottom));
    color: var(--white); text-align: center;
  }
  .info-column > div { position: absolute; width: 100%; }
  .badge {
    position: absolute; left: 642px; top: 364px; width: 272px; height: 272px; border-radius: 50%;
    background: var(--badge-orange); box-shadow: 0 8px 0 var(--badge-edge);
    text-align: center; padding-top: 44px; font-family: "Source Sans 3", sans-serif;
  }
  .badge p { font-style: italic; font-weight: 700; font-size: 24px; line-height: 28px; color: var(--badge-text); white-space: nowrap; }
  .badge strong { display: block; margin-top: 9px; font-size: 29px; line-height: 30px; color: var(--ink); text-transform: uppercase; }
  .hours { top: 174px; font-size: 17px; font-weight: 300; line-height: 23px; }
  .phone-main { top: 276px; font-size: 28px; font-weight: 700; }
  .pin-note { top: 334px; font-size: 17px; font-weight: 300; line-height: 23.3px; }
  .pin-note strong { font-weight: 700; }
  .line-label { top: 450px; font-size: 17px; font-weight: 300; }
  .phone-line { top: 467px; font-size: 24px; font-weight: 700; }
  .line-hint { top: 501px; font-size: 12.5px; font-style: italic; font-weight: 300; }
  .site { top: 542px; font-size: 17px; font-weight: 400; }

  .footer {
    position: absolute; left: 0; bottom: 0; width: 960px; height: 110px;
    background: var(--footer-navy); color: var(--white); text-align: center;
    font-family: "Source Sans 3", sans-serif;
  }
  .footer p { padding-top: 19px; font-size: 17px; font-weight: 700; line-height: 22px; text-transform: uppercase; }
  .footer small { position: absolute; right: 60px; bottom: 22px; font-family: "Open Sans", sans-serif; font-size: 11.5px; font-style: italic; font-weight: 300; }
</style>
</head>
<body>
  <div class="sky" role="img" aria-label="Bright blue sky filled with soft white clouds"></div>
  <div class="road-scene" role="img" aria-label="Couple driving a red convertible sports car down an open road"></div>

  <h1 class="headline">
    <span class="line-small">Lantern of</span>
    <span class="line-big">Quiet</span>
    <span class="line-red">Orchards</span>
  </h1>
  <p class="tagline">The best way to predict your future is to create it.</p>

  <h2 class="heading intro-title">What’s the #1 Success Factor<br>in Every Home-Based Business?</h2>
  <p class="copy intro-copy">The answer is <strong>DUPLICATION!</strong> The key to building a highly successful<br>homebased business is having a <strong>SYSTEM</strong> in place that everyone can<br>easily follow... <strong>WE HAVE THAT SYSTEM IN PLACE!</strong></p>
  <p class="copy system-copy">It’s a simple 3 steps proven postcard system that you can plug in<br>immediately. <i>The Entire Process Is Automated.</i></p>

  <h2 class="heading how-title">Here’s How It Works!</h2>
  <ol class="steps">
    <li><span class="step-num">1</span>Your prospects receive your postcard in the mail.</li>
    <li><span class="step-num">2</span>They listen to the 24-Hour Information Line and</li>
    <li><span class="step-num">3</span>They contact the Call Center to get their questions<br>answer and then close the sales for you.</li>
  </ol>

  <h2 class="heading never-title">You Never Have To Speak To Anyone!</h2>
  <ul class="benefits">
    <li><svg width="16" height="20" viewBox="0 0 16 20"><path d="M1 11 L5 18 L15 1" fill="none" stroke="#1d1d1f" stroke-width="3"/></svg>50% fast start bonuses <em>PAID WEEKLY!</em></li>
    <li><svg width="16" height="20" viewBox="0 0 16 20"><path d="M1 11 L5 18 L15 1" fill="none" stroke="#1d1d1f" stroke-width="3"/></svg>Receive a 100% Matching Bonus on all your personal sponsor<br>member’s income <em>PAID WEEKLY!</em></li>
    <li><svg width="16" height="20" viewBox="0 0 16 20"><path d="M1 11 L5 18 L15 1" fill="none" stroke="#1d1d1f" stroke-width="3"/></svg>One-of-a-kind <em>TWO TEAM</em> compensation plan!</li>
    <li><svg width="16" height="20" viewBox="0 0 16 20"><path d="M1 11 L5 18 L15 1" fill="none" stroke="#1d1d1f" stroke-width="3"/></svg>Receive the choice of <em>50 FREE POST CARDS</em> and <em>50 FREE</em><br><em>LEADS</em> or 20 home business surveyed leads with first month<br>product purchase!</li>
    <li><svg width="16" height="20" viewBox="0 0 16 20"><path d="M1 11 L5 18 L15 1" fill="none" stroke="#1d1d1f" stroke-width="3"/></svg>Receive <em>THREE</em> professional websites for your business for <em>FREE!</em></li>
    <li><svg width="16" height="20" viewBox="0 0 16 20"><path d="M1 11 L5 18 L15 1" fill="none" stroke="#1d1d1f" stroke-width="3"/></svg>Global business already shipping to over 45 countries worldwide<br>and expanding.</li>
    <li><svg width="16" height="20" viewBox="0 0 16 20"><path d="M1 11 L5 18 L15 1" fill="none" stroke="#1d1d1f" stroke-width="3"/></svg>30-Day - No Questions Asked, 100% Money Back Guarantee!</li>
  </ul>

  <aside class="info-column">
    <div class="hours">CALL CENTER HOURS<br>Monday thru Friday<br>12PM to 9PM EST<br>Saturday: 12PM to 5PM EST</div>
    <div class="phone-main">(555) 014-2736</div>
    <div class="pin-note">You will need the Call Center<br>Pin number when calling!<br><strong>Call Center Pin<br>Number: K7046</strong></div>
    <div class="line-label">24-Hour Information Line:</div>
    <div class="phone-line">(555) 019-3381</div>
    <div class="line-hint">(Listen before contacting the Call Center)</div>
    <div class="site">www.threequietsteps.com</div>
  </aside>

  <div class="badge">
    <p>100’s of people<br>are joining every day<br>and taking advantage<br>of this once-in-alifetime<br>opportunity.</p>
    <strong>Don’t Miss<br>Out!</strong>
  </div>

  <footer class="footer">
    <p>Due to the high volume of callers, if lines are busy, please keep trying to call into the call<br>center or you can just go to the website and get enrolled right away to secure a top position.</p>
    <small>© 2016 Brightfield Outreach Group</small>
  </footer>
</body>
</html>
```